Web App Dashboard Design for Healthcare Company

We have developed a simple web application with 3 navigation menus. We like the current design (very much modeled after Tallyworks), but we want to explore UI options for the branding, header, menus, and footer that we may not have considered.

The attached screenshots show the layout and two menu "hover" views as they currently exist.

This web application is used by employees only.

Menu 1 - Module Menu:
Allows the user to switch easily between Account, Employee, and Care Management.

Menu 2 - Reports Menu
Allows user to view available reports within each Module.

Menu 3 - Admin Menu
Allows the user to easily create new content types within each module.

Use our branded colors and font.

Colors:
Logo Blue (dark): 00c0f3
Logo Blue (light): 44c8f5
Nav Blue: 0994d0
Green: 71b44b
Grayscale: (not specified)

Font:
Lato (Google Font)

Target Market(s)

Internal staff.

Industry/Entity Type

Healthcare

Number of Pages Required

3 page

Font styles to use
Sans Serif
Other font styles liked:
• Lato (Google Font)

Colors
0293ce
9bcb3c

Requirements
Must have
• It's really a one page design, but we want to see the two "hover" views for the Module Menu and the Admin Menu.
• It should also be very clear which "Report" page the user is on (the active menu link).
• Must use branded colors, font, and logo.
• Logo Blue (dark): 00c0f3
• Logo Blue (light): 44c8f5
• Nav Blue: 0994d0
• Green: 71b44b
• Grayscale: Designer may choose
Nice to have
• It would be nice to have simple uncluttered payouts.
Should not have
• The design should not have menu options exposed by default.

```html
<!DOCTYPE html>
<html lang="en">
<head>
<meta charset="utf-8">
<title>Caretrail – Accounts Management</title>
<link href="https://fonts.googleapis.com/css2?family=Lato:wght@400;700&display=swap" rel="stylesheet">
<style>
:root{
  --logo-blue:#00c0f3;
  --logo-blue-light:#44c8f5;
  --nav-blue:#0994d0;
  --accent-blue:#3ab6e8;
  --green:#71b44b;
  --badge-green:#5aac3f;
  --badge-red:#f26d6d;
  --ink:#222;
  --text:#555;
  --rule:#e3e3e3;
  --panel:#f7f7f7;
  --head:#f2f2f2;
  --footer:#333;
}
*{box-sizing:border-box;margin:0;padding:0}
html,body{width:1200px;height:740px;overflow:hidden;background:#fff;font-family:'Lato',sans-serif;color:var(--ink)}
.app{position:relative;width:1200px;height:740px}

.sidebar{position:absolute;left:0;top:0;width:189px;height:698px;background:var(--panel);border-right:3px solid #e6e6e6}
.brand{height:100px;background:#fff;border-bottom:1px solid var(--rule);display:flex;align-items:center;justify-content:center;gap:8px}
.brand-mark{width:16px;height:16px;border-radius:50%;background:var(--logo-blue)}
.brand-name{font-size:26px;font-weight:700;color:#2a2a2a}
.nav-item{display:flex;height:56px;border-bottom:1px solid var(--rule);background:#fff}
.nav-icon{width:54px;border-right:1px solid var(--rule);display:flex;align-items:center;justify-content:center;color:#555}
.nav-label{display:flex;align-items:center;padding-left:19px;font-size:13px;color:#111}
.nav-item.active .nav-icon{background:var(--green);color:#fff;border-right:none}
.nav-item.active .nav-label{color:var(--green);font-weight:700}

.topbar{position:absolute;left:189px;top:0;right:0;height:100px}
.module-select{position:absolute;left:27px;top:32px;width:431px;height:37px;border:1px solid #ddd;display:flex;align-items:center;font-size:12px;padding-left:15px}
.module-select .caret{position:absolute;right:0;top:0;width:36px;height:100%;border-left:1px solid #ddd;display:flex;align-items:center;justify-content:center}
.my-info{position:absolute;left:781px;top:40px;font-size:12px}
.divider{position:absolute;left:843px;top:27px;width:1px;height:46px;background:#ddd}
.greeting{position:absolute;right:66px;top:33px;text-align:right;font-size:12px;line-height:16px}
.greeting .acct{display:inline-flex;align-items:center;gap:8px}
.avatar{position:absolute;right:26px;top:34px}
.accent-rule{position:absolute;left:189px;top:99px;right:0;height:3px;background:var(--accent-blue)}

.grid{position:absolute;left:189px;top:102px;width:1011px;border-collapse:collapse;table-layout:fixed;font-size:12px}
.grid th{height:45px;background:var(--head);font-weight:400;font-size:13px;text-align:left;padding-left:16px;border-right:1px solid var(--rule);border-bottom:1px solid var(--rule)}
.grid th.sorted{position:relative}
.grid th.sorted::after{content:"";position:absolute;right:16px;top:20px;border:4px solid transparent;border-bottom:5px solid var(--accent-blue);border-top:0}
.grid td{height:37.5px;color:var(--text);padding-left:15px;border-bottom:1px solid var(--rule);border-right:1px solid var(--rule)}
.grid td:first-child{padding-left:16px;border-bottom:1px solid var(--rule)}
.grid td.num{text-align:right;padding-right:14px}
.grid td.dash{text-align:center;padding-left:0}
.grid td.action{border-right:none;padding-left:21px}
.grid td.spacer,.grid th.spacer{border-right:none;border-bottom:none;background:#fff}
.grid th.spacer{background:var(--head);border-left:1px solid var(--rule)}
.badge{display:inline-block;width:83px;height:18px;line-height:18px;text-align:center;color:#fff;font-size:10.5px;border-radius:3px}
.badge.overdue{background:var(--badge-red)}
.badge.ok{background:var(--badge-green)}
.btn-cancel{display:inline-block;width:70px;height:17px;line-height:17px;border-radius:3px;background:var(--accent-blue);color:#fff;font-size:10.5px;text-align:center}
.side-rule{position:absolute;left:1174px;top:146px;width:1px;height:478px;background:var(--rule)}

.per-page{position:absolute;left:206px;top:634px;display:flex;align-items:center;gap:11px;font-size:11px}
.per-page .select{width:79px;height:26px;border:1px solid #ddd;position:relative;padding-left:10px;line-height:24px;font-size:11px}
.per-page .select .step{position:absolute;right:0;top:0;width:28px;height:100%;border-left:1px solid #ddd;display:flex;align-items:center;justify-content:center}
.pager{position:absolute;left:902px;top:635px;display:flex;align-items:center;gap:6px;font-size:11px}
.pager .pg{width:21px;height:20px;border:1px solid #ccc;display:flex;align-items:center;justify-content:center;color:#333}
.pager .pg.current{background:var(--logo-blue-light);border-color:var(--logo-blue-light);color:#fff}
.pager .gap{width:60px;border-top:2px dotted #333;margin:0 1px}
.fade{position:absolute;left:280px;top:688px;width:860px;height:3px;background:radial-gradient(ellipse at center,#ddd,transparent 70%)}

.footer{position:absolute;left:0;bottom:0;width:1200px;height:42px;background:var(--footer);color:#fff;font-size:12px;display:flex;align-items:center;justify-content:space-between;padding:0 28px 0 34px}
</style>
</head>
<body>
<div class="app">
  <aside class="sidebar">
    <div class="brand"><span class="brand-mark"></span><span class="brand-name">Caretrail</span></div>
    <nav>
      <div class="nav-item active"><div class="nav-icon">
        <svg width="24" height="24" viewBox="0 0 24 24" fill="none" stroke="#fff" stroke-width="1.6"><rect x="4" y="3" width="13" height="17" rx="1"/><path d="M7 7h7M7 10h5M7 13h4"/><circle cx="17" cy="16" r="4.5" fill="var(--green)"/><path d="M17 14v2.3l1.5 1"/></svg>
      </div><div class="nav-label">Reminders</div></div>
      <div class="nav-item"><div class="nav-icon">
        <svg width="24" height="20" viewBox="0 0 24 20" fill="#555"><circle cx="12" cy="6" r="3.5"/><circle cx="5" cy="7" r="2.6"/><circle cx="19" cy="7" r="2.6"/><path d="M5 18c0-4 3-6.5 7-6.5s7 2.5 7 6.5z"/><path d="M0 17c0-3 2-5 5-5 1 0 2 .3 2.5.8C5.5 14 4.5 15.5 4.3 17z"/><path d="M24 17c0-3-2-5-5-5-1 0-2 .3-2.5.8 2 1.2 3 2.7 3.2 4.2z"/></svg>
      </div><div class="nav-label">Accounts</div></div>
      <div class="nav-item"><div class="nav-icon">
        <svg width="22" height="24" viewBox="0 0 22 24" fill="none" stroke="#555" stroke-width="1.6"><circle cx="11" cy="7" r="4.5"/><path d="M2 22c0-5 4-8 9-8s9 3 9 8z" fill="#555"/><circle cx="15" cy="18" r="2" fill="#fff" stroke="none"/></svg>
      </div><div class="nav-label">Patient Requests</div></div>
      <div class="nav-item"><div class="nav-icon">
        <svg width="20" height="26" viewBox="0 0 20 26" fill="none" stroke="#555" stroke-width="1.6"><rect x="2" y="3" width="16" height="21" rx="1"/><rect x="7" y="1" width="6" height="4" fill="#555"/><path d="M6 20v-4M10 20v-7M14 20v-5"/><circle cx="12" cy="9" r="2"/></svg>
      </div><div class="nav-label">Reports</div></div>
      <div class="nav-item"><div class="nav-icon">
        <svg width="24" height="24" viewBox="0 0 24 24" fill="none" stroke="#555" stroke-width="1.6"><rect x="2" y="4" width="12" height="18"/><rect x="14" y="9" width="8" height="13"/><path d="M5 8h2M9 8h2M5 12h2M9 12h2M5 16h2M9 16h2M17 13h2M17 17h2"/></svg>
      </div><div class="nav-label">My Company</div></div>
    </nav>
  </aside>

  <header class="topbar">
    <div class="module-select">Accounts Management
      <span class="caret"><svg width="10" height="6" viewBox="0 0 10 6"><path d="M0 0h10L5 6z" fill="#bbb"/></svg></span>
    </div>
    <div class="my-info">My Info</div>
    <div class="divider"></div>
    <div class="greeting">Hello Mira Lane,<br><span class="acct"><svg width="9" height="6" viewBox="0 0 9 6"><path d="M1 1l3.5 3.5L8 1" stroke="var(--green)" stroke-width="1.6" fill="none"/></svg>Account</span></div>
    <svg class="avatar" width="32" height="32" viewBox="0 0 32 32" fill="none" stroke="var(--logo-blue)" stroke-width="2"><circle cx="16" cy="16" r="14.5"/><circle cx="16" cy="12.5" r="5"/><path d="M7 26c2-5 5-7 9-7s7 2 9 7"/></svg>
  </header>
  <div class="accent-rule"></div>

  <table class="grid">
    <colgroup><col style="width:115px"><col style="width:168px"><col style="width:84px"><col style="width:136px"><col style="width:126px"><col style="width:242px"><col style="width:114px"><col style="width:26px"></colgroup>
    <thead><tr><th>Lorem ipsum</th><th class="sorted">consectur scing</th><th>laoreet</th><th>cursus sagittis</th><th>accumsalestie</th><th>tincidunt dolor</th><th></th><th class="spacer"></th></tr></thead>
    <tbody>
      <tr><td><span class="badge overdue">accumsan</span></td><td class="num">01 213 456 789</td><td>Maecenas</td><td>Donec nec velit</td><td class="dash">–</td><td>Donec sollicitudin neque</td><td class="action"><span class="btn-cancel">cancel</span></td><td class="spacer"></td></tr>
      <tr><td><span class="badge overdue">accumsan</span></td><td class="num">01 213 456 789</td><td>placerat</td><td>aliquam</td><td class="dash">–</td><td>at nisi dignissim</td><td class="action"><span class="btn-cancel">cancel</span></td><td class="spacer"></td></tr>
      <tr><td><span class="badge overdue">accumsan</span></td><td class="num">01 213 456 789</td><td>turpis</td><td>bibendum purus</td><td class="dash">–</td><td>onsectetur id id metus</td><td class="action"><span class="btn-cancel">cancel</span></td><td class="spacer"></td></tr>
      <tr><td><span class="badge overdue">accumsan</span></td><td class="num">01 213 456 789</td><td>consees</td><td>eget feugiat eros</td><td class="dash">–</td><td>Fusce condimentum metus sed</td><td class="action"><span class="btn-cancel">cancel</span></td><td class="spacer"></td></tr>
      <tr><td><span class="badge ok">est viverra</span></td><td class="num">01 213 456 789</td><td>viverra</td><td>bibendum purus</td><td class="dash">–</td><td>ex facilisis, vel tincidunt</td><td class="action"><span class="btn-cancel">cancel</span></td><td class="spacer"></td></tr>
      <tr><td><span class="badge ok">est viverra</span></td><td class="num">01 213 456 789</td><td>nec</td><td>eget feugiat eros</td><td class="dash">–</td><td>dolor ultrices Suspendisse</td><td class="action"><span class="btn-cancel">cancel</span></td><td class="spacer"></td></tr>
      <tr><td><span class="badge ok">est viverra</span></td><td class="num">01 213 456 789</td><td>bibendu</td><td>Donec nec velit</td><td class="dash">–</td><td>et ligula euismod dapibus nisi</td><td class="action"><span class="btn-cancel">cancel</span></td><td class="spacer"></td></tr>
      <tr><td><span class="badge ok">est viverra</span></td><td class="num">01 213 456 789</td><td>lacus</td><td>aliquam</td><td class="dash">–</td><td>eu po euismod rta erat</td><td class="action"><span class="btn-cancel">cancel</span></td><td class="spacer"></td></tr>
      <tr><td><span class="badge ok">est viverra</span></td><td class="num">01 213 456 789</td><td>efficitupl</td><td>bibendum purus</td><td class="dash">–</td><td>nsectetur id id metus</td><td class="action"><span class="btn-cancel">cancel</span></td><td class="spacer"></td></tr>
      <tr><td><span class="badge ok">est viverra</span></td><td class="num">01 213 456 789</td><td>turpis</td><td>eget feugiat eros</td><td class="dash">–</td><td>Fusce condimentum metus sed</td><td class="action"><span class="btn-cancel">cancel</span></td><td class="spacer"></td></tr>
      <tr><td><span class="badge ok">est viverra</span></td><td class="num">01 213 456 789</td><td>consees</td><td>bibendum purus</td><td class="dash">–</td><td>ex facilisis, vel tincidunt</td><td class="action"><span class="btn-cancel">cancel</span></td><td class="spacer"></td></tr>
      <tr><td><span class="badge ok">est viverra</span></td><td class="num">01 213 456 789</td><td>viverra</td><td>Donec nec velit</td><td class="dash">–</td><td>dolor ultrices Suspendisse</td><td class="action"><span class="btn-cancel">cancel</span></td><td class="spacer"></td></tr>
    </tbody>
  </table>
  <div class="side-rule"></div>

  <div class="per-page">Per Page
    <div class="select">12<span class="step"><svg width="7" height="10" viewBox="0 0 7 10"><path d="M0 4h7L3.5 0zM0 6h7L3.5 10z" fill="#333"/></svg></span></div>
  </div>
  <nav class="pager">
    <span class="pg"><svg width="6" height="9" viewBox="0 0 6 9"><path d="M5 1L1.5 4.5 5 8" stroke="#333" stroke-width="1.4" fill="none"/></svg></span>
    <span class="pg current">1</span><span class="pg">2</span><span class="pg">3</span><span class="pg">4</span><span class="pg">5</span>
    <span class="gap"></span>
    <span class="pg"><svg width="6" height="9" viewBox="0 0 6 9"><path d="M1 1l3.5 3.5L1 8" stroke="#333" stroke-width="1.4" fill="none"/></svg></span>
  </nav>
  <div class="fade"></div>

  <footer class="footer"><span>© 2017 Caretrail. All Right reserved</span><span>Contact Us</span></footer>
</div>
</body>
</html>
```